International Education App needs UI Design

My current app is being upgraded and totally rebranded. This app is aimed to become No1. communication app for schools worldwide. Aimed at parents and high school students it will have events, assessments, messages, newsletters, notes, policies, contact us plus much more.
It will need to be much engaging and professional than all other apps on the market. You can see them attached to compare as well as the app logo to tie in the design. You can also see my current app and why needs an upgrade.
There will need to be design for each screen.
Needs a slick and professional finish with Tranvelo Blue as the base colour.
The app is called ClassNook
You will also find a file attached which shows functionality which will help design screens.

Target Market(s)

Parents, High Schools Students

Industry/Entity Type

Education

Font styles to use
Sans Serif

Colors
0355a3

Requirements
Must have
• Sleek, modern, professional and better than examples provided.
• I need a splash screen, home screen and each of the other screens designed.

```html
<!DOCTYPE html>
<html lang="en">
<head>
<meta charset="utf-8">
<title>ClassNook – Home</title>
<link href="https://fonts.googleapis.com/css2?family=Open+Sans:wght@400;600&display=swap" rel="stylesheet">
<style>
  :root {
    --brand-blue: #0355a3;
    --brand-blue-bright: #1565c8;
    --badge-blue: #0b5fc0;
    --white: #ffffff;
    --band-text: #2f7fd0;
    --row-dark: rgba(20, 16, 14, 0.62);
    --row-mid: rgba(40, 34, 30, 0.45);
    --row-line: rgba(255, 255, 255, 0.18);
    --icon-ring: #3b3b3b;
    --page-bg: #f2f2f2;
  }
  * { box-sizing: border-box; margin: 0; padding: 0; }
  html, body {
    width: 1200px; height: 2352px; overflow: hidden;
    background: var(--page-bg);
    font-family: "Open Sans", Helvetica, Arial, sans-serif;
  }
  .screen {
    position: relative; width: 1200px; height: 2352px; overflow: hidden;
    background: var(--white);
  }
  .status-bar {
    height: 64px; background: var(--brand-blue); color: var(--white);
    display: flex; align-items: center; justify-content: space-between;
    padding: 0 26px; font-size: 36px; font-weight: 600;
  }
  .status-left, .status-right { display: flex; align-items: center; gap: 14px; width: 380px; }
  .status-right { justify-content: flex-end; }
  .signal { display: flex; gap: 5px; }
  .signal span { width: 15px; height: 15px; border-radius: 50%; background: var(--white); }
  .signal span.off { background: transparent; border: 2px solid var(--white); }
  .nav-bar {
    height: 196px; background: var(--brand-blue); color: var(--white);
    display: flex; align-items: center; justify-content: center; position: relative;
  }
  .nav-title { font-size: 60px; font-weight: 400; }
  .menu-button { position: absolute; right: 46px; top: 66px; width: 96px; height: 64px; }
  .school-band {
    height: 230px; background: var(--white);
    display: flex; align-items: center; padding: 0 64px; gap: 56px;
    position: relative;
  }
  .school-band::after {
    content: ""; position: absolute; left: 64px; bottom: 18px; width: 300px; height: 3px;
    background: #d5d5d5;
  }
  .school-mark { width: 170px; height: 170px; border-radius: 26px; background: var(--brand-blue-bright); flex: none; }
  .school-name { font-size: 58px; color: var(--band-text); font-weight: 400; white-space: nowrap; }
  .menu-area { position: relative; height: 1862px; }
  .menu-backdrop {
    position: absolute; inset: 0;
    background: radial-gradient(ellipse at 45% 30%, #c99577 0%, #8a5d48 35%, #4b3a33 70%, #2c2522 100%);
  }
  .menu-list { position: relative; list-style: none; }
  .menu-item {
    height: 258px; display: flex; align-items: center; padding: 0 44px 0 28px;
    background: var(--row-dark); border-bottom: 3px solid var(--row-line);
    color: var(--white);
  }
  .menu-item.is-light { background: var(--row-mid); }
  .menu-icon {
    width: 200px; height: 200px; border-radius: 50%;
    background: var(--icon-ring); border: 6px solid rgba(255,255,255,0.75);
    display: flex; align-items: center; justify-content: center; flex: none;
  }
  .menu-icon svg { width: 118px; height: 118px; }
  .menu-label { font-size: 54px; margin-left: 56px; flex: 1; }
  .menu-count {
    width: 64px; height: 64px; border-radius: 50%; background: var(--badge-blue);
    font-size: 32px; font-weight: 600; display: flex; align-items: center; justify-content: center;
    margin-right: 40px;
  }
  .menu-chevron { width: 36px; height: 64px; }
</style>
</head>
<body>
<main class="screen">
  <header>
    <div class="status-bar">
      <div class="status-left">
        <div class="signal"><span></span><span></span><span></span><span class="off"></span><span class="off"></span></div>
        <span>VOLTA</span>
        <svg width="44" height="34" viewBox="0 0 44 34" aria-hidden="true"><path d="M4 12a26 26 0 0 1 36 0M10 19a17 17 0 0 1 24 0M16 26a8 8 0 0 1 12 0" fill="none" stroke="#fff" stroke-width="4" stroke-linecap="round"/><circle cx="22" cy="31" r="3" fill="#fff"/></svg>
      </div>
      <span class="status-time">4:21 PM</span>
      <div class="status-right">
        <svg width="22" height="38" viewBox="0 0 22 38" aria-hidden="true"><path d="M3 10l16 17-8 8V3l8 8L3 28" fill="none" stroke="#fff" stroke-width="3" stroke-linejoin="round"/></svg>
        <span>100%</span>
        <svg width="78" height="36" viewBox="0 0 78 36" aria-hidden="true"><rect x="2" y="4" width="66" height="28" rx="5" fill="none" stroke="#fff" stroke-width="3"/><rect x="7" y="9" width="56" height="18" rx="2" fill="#fff"/><rect x="70" y="12" width="5" height="12" rx="2" fill="#fff"/></svg>
      </div>
    </div>
    <nav class="nav-bar">
      <h1 class="nav-title">Home</h1>
      <svg class="menu-button" viewBox="0 0 96 64" aria-label="Menu"><rect y="2" width="96" height="7" fill="#fff"/><rect y="29" width="96" height="7" fill="#fff"/><rect y="56" width="96" height="7" fill="#fff"/></svg>
    </nav>
  </header>

  <section class="school-band">
    <div class="school-mark" aria-hidden="true"></div>
    <p class="school-name">Northcliff Heights Public School</p>
  </section>

  <section class="menu-area">
    <div class="menu-backdrop" role="img" aria-label="Soft-focus photo of a smiling school child"></div>
    <ul class="menu-list">
      <li class="menu-item">
        <span class="menu-icon"><svg viewBox="0 0 60 60" aria-hidden="true"><path d="M14 20l16-8 16 8-16 7z" fill="#fff"/><circle cx="30" cy="30" r="10" fill="#fff"/><path d="M12 56c2-12 9-17 18-17s16 5 18 17z" fill="#fff"/></svg></span>
        <span class="menu-label">Students</span>
        <span class="menu-count">25</span>
        <svg class="menu-chevron" viewBox="0 0 36 64" aria-hidden="true"><path d="M6 6l24 26L6 58" fill="none" stroke="#fff" stroke-width="5"/></svg>
      </li>
      <li class="menu-item is-light">
        <span class="menu-icon"><svg viewBox="0 0 60 60" aria-hidden="true"><rect x="6" y="12" width="40" height="38" rx="3" fill="none" stroke="#fff" stroke-width="3"/><rect x="6" y="12" width="40" height="9" fill="#fff"/><text x="26" y="44" fill="#fff" font-size="17" font-family="Open Sans, sans-serif" text-anchor="middle">12</text><circle cx="45" cy="44" r="11" fill="#3b3b3b" stroke="#fff" stroke-width="3"/><path d="M45 38v6h5" stroke="#fff" stroke-width="2.5" fill="none"/></svg></span>
        <span class="menu-label">Events</span>
        <span class="menu-count">7</span>
        <svg class="menu-chevron" viewBox="0 0 36 64" aria-hidden="true"><path d="M6 6l24 26L6 58" fill="none" stroke="#fff" stroke-width="5"/></svg>
      </li>
      <li class="menu-item">
        <span class="menu-icon"><svg viewBox="0 0 60 60" aria-hidden="true"><rect x="6" y="14" width="48" height="32" fill="#fff"/><path d="M6 14l24 18 24-18" fill="none" stroke="#3b3b3b" stroke-width="3"/></svg></span>
        <span class="menu-label">Messages</span>
        <span class="menu-count">1</span>
        <svg class="menu-chevron" viewBox="0 0 36 64" aria-hidden="true"><path d="M6 6l24 26L6 58" fill="none" stroke="#fff" stroke-width="5"/></svg>
      </li>
      <li class="menu-item">
        <span class="menu-icon"><svg viewBox="0 0 60 60" aria-hidden="true"><rect x="12" y="8" width="38" height="44" fill="none" stroke="#fff" stroke-width="3"/><rect x="17" y="14" width="12" height="12" fill="#fff"/><path d="M33 16h12M33 22h12M17 32h28M17 38h28M17 44h28" stroke="#fff" stroke-width="2.5"/><path d="M12 16H6v32a4 4 0 0 0 6 4" fill="none" stroke="#fff" stroke-width="3"/></svg></span>
        <span class="menu-label">Newsletters</span>
        <span class="menu-count">6</span>
        <svg class="menu-chevron" viewBox="0 0 36 64" aria-hidden="true"><path d="M6 6l24 26L6 58" fill="none" stroke="#fff" stroke-width="5"/></svg>
      </li>
      <li class="menu-item is-light">
        <span class="menu-icon"><svg viewBox="0 0 60 60" aria-hidden="true"><rect x="10" y="10" width="34" height="42" fill="none" stroke="#fff" stroke-width="3"/><path d="M16 20h20M16 28h20M16 36h12" stroke="#fff" stroke-width="2.5"/><path d="M52 16L32 44l-5 3 1-6 20-28z" fill="#fff"/></svg></span>
        <span class="menu-label">Notes</span>
        <span class="menu-count">4</span>
        <svg class="menu-chevron" viewBox="0 0 36 64" aria-hidden="true"><path d="M6 6l24 26L6 58" fill="none" stroke="#fff" stroke-width="5"/></svg>
      </li>
      <li class="menu-item">
        <span class="menu-icon"><svg viewBox="0 0 60 60" aria-hidden="true"><path d="M18 36a10 10 0 0 1-2-19 12 12 0 0 1 28 0 10 10 0 0 1-2 19z" fill="#fff"/><rect x="18" y="38" width="24" height="14" rx="2" fill="#fff"/><path d="M25 42v7M30 42v7M35 42v7" stroke="#3b3b3b" stroke-width="2"/></svg></span>
        <span class="menu-label">Canteen</span>
        <span class="menu-count">3</span>
        <svg class="menu-chevron" viewBox="0 0 36 64" aria-hidden="true"><path d="M6 6l24 26L6 58" fill="none" stroke="#fff" stroke-width="5"/></svg>
      </li>
      <li class="menu-item is-light">
        <span class="menu-icon"></span>
      </li>
    </ul>
  </section>
</main>
</body>
</html>
```